Website Layout for PanFolio

PanFolio is a company that will be dedicated (for now) to publishing recipes with the nutrition facts. Run by a nutritionist. In the future there may be a mobile app.

We need layout for 3 of the pages of the website. NO PROGRAMMING, only layout and graphic design. Not very complicated.

--Please view the details in the attached document--
We want a layout design for the pages: P.01, P.02 and P.03

Logo is also attached. Please don't hesitate if you want to modify the logo to fit your idea. The design should be clean, visually attractive and refreshing to look at. It should be sleek and a feel of technology, yet also natural and culinary.

Some examples to get ideas:

http://www.marlowhearthtales.com/
http://www.tavelbrunefare.org/site/
http://thecobaltladle.com/products/dice-deck
Updates

Project Deadline Extended
Reason: I extend the deadline for this week to allow you space for work on the observations made to your design and to provide the P.02 and P.03 designs. We greatly appreciate your hard work and are thrilled with your ideas.

Target Market(s)

Young people that live alone or want to optimize their cooking.
Young, modern housewives with a smartphone.

Industry/Entity Type

Nutrition

Requirements
Must have
• --Please view the details in the attached document--
NO PROGRAMMING. Only layout and graphic design.

```html
<!DOCTYPE html>
<html lang="en">
<head>
<meta charset="utf-8">
<title>PanFolio – Website Layout</title>
<link href="https://fonts.googleapis.com/css2?family=Raleway:wght@300;400;600;700&family=Poiret+One&family=Open+Sans:wght@400;600;700&display=swap" rel="stylesheet">
<style>
  :root{
    --canvas:#ebebeb;
    --page:#f2f2f2;
    --band:#e5e5e5;
    --ink:#2e2e2e;
    --muted:#6d6d6d;
    --taupe:#8c7b75;
    --rose:#c6aba3;
    --green:#a6ba2d;
    --button:#9c8f8a;
    --logo-ink:#3a3a3a;
    --logo-square:#e0612d;
    --rule:#cfcfcf;
  }
  *{box-sizing:border-box;margin:0;padding:0}
  html,body{width:1200px;height:1000px;overflow:hidden}
  body{background:var(--canvas);font-family:"Open Sans",Arial,sans-serif;color:var(--ink);position:relative}

  .board-label{position:absolute;top:150px;font-family:"Raleway",Arial,sans-serif;font-weight:400;font-size:18px;color:#6a6a6a}

  .page{position:absolute;background:var(--page);box-shadow:0 1px 4px rgba(0,0,0,.18);overflow:hidden}
  .page--main{left:140px;top:215px;width:294px;height:558px}
  .page--list{left:462px;top:215px;width:295px;height:528px}
  .page--recipe{left:783px;top:215px;width:296px;height:432px}

  .abs{position:absolute}

  /* brand */
  .brand{position:absolute;left:0;right:0;top:30px;display:flex;justify-content:center;align-items:center;gap:4px}
  .brand__square{width:11px;height:11px;background:var(--logo-square)}
  .brand__name{font-family:"Raleway",Arial,sans-serif;font-weight:700;font-size:17px;color:var(--logo-ink);letter-spacing:-.2px}

  .social{position:absolute;left:44px;top:17px;display:flex;gap:9px}
  .social span{width:5px;height:5px;border-radius:50%;background:#4a4a4a}
  .search{position:absolute;left:203px;top:15px;width:46px;height:9px;border:1px solid #c9c9c9;border-radius:1px;font-size:3.5px;color:#999;padding:1px 0 0 8px;background:#f7f7f7}
  .search::before{content:"";position:absolute;left:2px;top:2px;width:3px;height:3px;border:.6px solid #999;border-radius:50%}

  .nav{position:absolute;left:0;right:0;display:flex;justify-content:center;gap:14px;font-family:"Raleway",Arial,sans-serif;font-weight:600;font-size:4px;color:#444;letter-spacing:.2px}
  .nav .sep{color:#999}
  .nav .is-active{color:var(--green)}

  .photo{position:absolute}
  .photo--hero-main{left:0;top:88px;width:294px;height:104px;background:linear-gradient(100deg,#5c6a3a 0%,#2f3a25 35%,#3c4a2c 60%,#7a3a24 85%,#4a3d2a 100%)}
  .photo--hero-main::after{content:"";position:absolute;inset:0;background:rgba(20,28,18,.35)}
  .hero-copy{position:absolute;left:0;right:0;top:27px;text-align:center;color:#fff;z-index:1}
  .hero-copy h1{font-family:"Poiret One",Arial,sans-serif;font-weight:400;font-size:11px;letter-spacing:.4px}
  .hero-copy p{width:180px;margin:3px auto 0;font-size:4px;line-height:5px;text-transform:uppercase}
  .hero-copy .auth{margin-top:8px;font-family:"Raleway",Arial,sans-serif;font-size:4.5px;display:flex;justify-content:center;gap:18px}

  .band{position:absolute;left:0;width:100%}
  .band--featured{top:398px;height:160px;background:var(--band)}

  .section-title{position:absolute;font-family:"Raleway",Arial,sans-serif;font-weight:300;letter-spacing:.3px}
  .section-title--center{left:0;right:0;text-align:center;font-size:12px;color:var(--rose)}
  .btn{display:block;background:var(--button);color:#fff;font-size:2.8px;text-align:center;line-height:4px;height:4px;font-family:"Open Sans",Arial,sans-serif}
  .btn--view-all{position:absolute;left:232px;top:226px;width:17px;background:#b9aaa5}

  .grid{position:absolute;left:45px;display:grid;grid-template-columns:repeat(4,47px);column-gap:6px}
  .cat-label{font-family:"Poiret One",Arial,sans-serif;font-size:6px;color:#333;margin-bottom:5px;white-space:nowrap}
  .thumb{height:35px}
  .thumb--bowl{background:linear-gradient(135deg,#4a3a4a,#6b4a3a 50%,#3b4a30)}
  .thumb--plate{background:linear-gradient(135deg,#e6dcd2,#b98a5a 55%,#7a5030)}
  .thumb--crumble{background:linear-gradient(135deg,#c35a2a,#8a3a1a 60%,#d07a40)}
  .thumb--drink{background:linear-gradient(135deg,#2f4a22,#7ca83a 50%,#3a5a2a)}

  .card__title{font-size:3.6px;font-weight:700;margin-top:6px;text-transform:uppercase}
  .card__meta{font-size:2.8px;color:var(--muted);margin-top:2px;line-height:3.6px;text-transform:uppercase}
  .card__desc{font-size:2.8px;color:#555;margin-top:2px;line-height:3.4px;text-transform:uppercase;height:21px}
  .card .btn{width:13px;margin:3px 0 0 auto}
  .card .btn--center{margin:3px auto 0}

  /* list page */
  .photo--hero-list{left:0;top:83px;width:295px;height:81px;background:linear-gradient(90deg,#3a2c22 0%,#2b3e6e 25%,#dfe3ec 38%,#3a2c22 55%,#5d6f8e 75%,#c9b08a 90%,#4a3a2a 100%)}
  .section-title--left{font-size:12px;color:var(--taupe)}
  .rule{position:absolute;height:1px;background:var(--rule)}
  .cats{position:absolute;left:46px;display:grid;grid-template-columns:repeat(4,51px);row-gap:6px;font-family:"Poiret One",Arial,sans-serif;font-size:6px;color:var(--taupe)}
  .cats .is-active{color:var(--green)}
  .pager{position:absolute;left:75px;top:492px;display:flex;gap:15px;font-size:5px;color:#444}
  .pager .is-active{color:var(--green);font-weight:700}

  /* recipe page */
  .category-tag{font-family:"Raleway",Arial,sans-serif;font-size:5px;color:var(--green);letter-spacing:.3px}
  .recipe-title{font-family:"Raleway",Arial,sans-serif;font-weight:400;font-size:10px;color:var(--taupe)}
  .recipe-date{font-size:3.6px;color:#444}
  .btn--print{position:absolute;left:215px;top:118px;width:35px;height:9px;line-height:9px;font-size:3.6px;display:flex;align-items:center;justify-content:center;gap:3px}
  .photo--detail-a{left:46px;top:135px;width:92px;height:81px;background:linear-gradient(135deg,#6a2a12,#c86a2a 45%,#8a3a18 75%,#3a1a0c)}
  .photo--detail-b{left:141px;top:135px;width:109px;height:81px;background:linear-gradient(135deg,#2f3a4a,#6a7fa8 40%,#c9b08a 65%,#8a2a2a 85%,#3a2a22)}
  .facts{position:absolute;left:46px;top:226px;width:204px;height:78px;background:var(--band);padding:6px 7px}
  .facts h2{font-family:"Raleway",Arial,sans-serif;font-weight:400;font-size:9px;color:var(--taupe);border-bottom:1px solid var(--rule);padding-bottom:2px}
  .facts dl{display:grid;grid-template-columns:51px 51px 51px 40px;row-gap:4px;margin-top:4px;font-size:3.8px;line-height:4.6px}
  .facts dt{color:#555}
  .facts dd{font-weight:700;color:#333}
  .block-title{font-family:"Raleway",Arial,sans-serif;font-weight:400;font-size:9px;color:var(--taupe)}
  .block-text{font-size:4px;line-height:5.2px;color:#222;font-weight:600}
</style>
</head>
<body>

<div class="board-label" style="left:140px">Main Page</div>
<div class="board-label" style="left:462px">Recipe list page</div>
<div class="board-label" style="left:783px">Recipe page</div>

<!-- MAIN PAGE -->
<section class="page page--main">
  <div class="social"><span></span><span></span><span></span><span></span></div>
  <div class="search">search</div>
  <div class="brand"><span class="brand__square"></span><span class="brand__name">PanFolio</span></div>
  <nav class="nav" style="top:79px"><span>ABOUT US</span><span class="sep">|</span><span>CONTACT</span></nav>

  <div class="photo photo--hero-main" role="img" aria-label="Photo of fresh vegetables and salad ingredients on a table">
    <div class="hero-copy">
      <h1>WELCOME TEXT</h1>
      <p>Lorem ipsum dolor sit amet, consectetur adipisicing elit, sed do eiusmod tempor incididunt ut labore et dolore magna aliqua. Ut enim ad minim veniam, quis nostrud exercitation ullamco laboris nisi ut aliquip ex ea commodo se cillum dolore eu fugiat nulla.</p>
      <div class="auth"><span>LOG IN</span><span>/</span><span>REGISTER</span></div>
    </div>
  </div>

  <h2 class="section-title section-title--center" style="top:216px">RECIPES</h2>
  <span class="btn btn--view-all">VIEW ALL</span>

  <div class="grid" style="top:250px">
    <div><div class="cat-label">BREAKFAST</div><div class="thumb thumb--bowl" role="img" aria-label="Photo of a grain bowl"></div></div>
    <div><div class="cat-label">MAIN DISH</div><div class="thumb thumb--plate" role="img" aria-label="Photo of a plated main dish"></div></div>
    <div><div class="cat-label">SALAD</div><div class="thumb thumb--crumble" role="img" aria-label="Photo of a baked dish on a spoon"></div></div>
    <div><div class="cat-label">LOREM IPSUM</div><div class="thumb thumb--drink" role="img" aria-label="Photo of a green drink"></div></div>
  </div>
  <div class="grid" style="top:318px">
    <div><div class="cat-label">BREAKFAST</div><div class="thumb thumb--bowl" role="img" aria-label="Photo of a grain bowl"></div></div>
    <div><div class="cat-label">MAIN DISH</div><div class="thumb thumb--plate" role="img" aria-label="Photo of a plated main dish"></div></div>
    <div><div class="cat-label">SALAD</div><div class="thumb thumb--crumble" role="img" aria-label="Photo of a baked dish on a spoon"></div></div>
    <div><div class="cat-label">LOREM IPSUM</div><div class="thumb thumb--drink" role="img" aria-label="Photo of a green drink"></div></div>
  </div>

  <div class="band band--featured"></div>
  <h2 class="section-title section-title--center" style="top:418px">FEATURED RECIPES</h2>
  <div class="grid" style="top:442px">
    <article class="card"><div class="thumb thumb--bowl" role="img" aria-label="Photo of a grain bowl"></div><h3 class="card__title">Recipe title</h3><p class="card__meta">320 calories<br>25 min</p><p class="card__desc">Fresh grains and bright greens with a quick lemon dressing.</p><span class="btn btn--center">MORE</span></article>
    <article class="card"><div class="thumb thumb--plate" role="img" aria-label="Photo of a plated main dish"></div><h3 class="card__title">Recipe title</h3><p class="card__meta">320 calories<br>25 min</p><p class="card__desc">Fresh grains and bright greens with a quick lemon dressing.</p><span class="btn btn--center">MORE</span></article>
    <article class="card"><div class="thumb thumb--crumble" role="img" aria-label="Photo of a baked dish on a spoon"></div><h3 class="card__title">Recipe title</h3><p class="card__meta">320 calories<br>25 min</p><p class="card__desc">Fresh grains and bright greens with a quick lemon dressing.</p><span class="btn btn--center">MORE</span></article>
    <article class="card"><div class="thumb thumb--drink" role="img" aria-label="Photo of a green drink"></div><h3 class="card__title">Recipe title</h3><p class="card__meta">320 calories<br>25 min</p><p class="card__desc">Fresh grains and bright greens with a quick lemon dressing.</p><span class="btn btn--center">MORE</span></article>
  </div>
</section>

<!-- RECIPE LIST PAGE -->
<section class="page page--list">
  <div class="brand"><span class="brand__square"></span><span class="brand__name">PanFolio</span></div>
  <nav class="nav" style="top:74px"><span>MAIN</span><span class="sep">|</span><span class="is-active">RECIPES</span><span class="sep">|</span><span>ABOUT</span><span class="sep">|</span><span>CONTACT</span></nav>

  <div class="photo photo--hero-list" role="img" aria-label="Photo of a breakfast table with granola, berries and a checked cloth"></div>

  <h2 class="section-title section-title--left" style="left:46px;top:179px">RECIPES</h2>
  <div class="rule" style="left:46px;top:199px;width:202px"></div>
  <div class="cats" style="top:211px">
    <span class="is-active">BREAKFAST</span><span>MAIN DISH</span><span>SALAD</span><span>CATEGORY</span>
    <span>CATEGORY</span><span>CATEGORY</span><span>CATEGORY</span><span>CATEGORY</span>
  </div>

  <div class="grid" style="top:249px;left:46px;grid-template-columns:repeat(4,47px);column-gap:5.5px">
    <article class="card"><div class="thumb thumb--bowl" role="img" aria-label="Photo of a grain bowl"></div><h3 class="card__title">Recipe title</h3><p class="card__meta">320 calories<br>25 min</p><p class="card__desc">Fresh grains and bright greens with a quick lemon dressing.</p><span class="btn">MORE</span></article>
    <article class="card"><div class="thumb thumb--plate" role="img" aria-label="Photo of a plated main dish"></div><h3 class="card__title">Recipe title</h3><p class="card__meta">320 calories<br>25 min</p><p class="card__desc">Fresh grains and bright greens with a quick lemon dressing.</p><span class="btn">MORE</span></article>
    <article class="card"><div class="thumb thumb--crumble" role="img" aria-label="Photo of a baked dish on a spoon"></div><h3 class="card__title">Recipe title</h3><p class="card__meta">320 calories<br>25 min</p><p class="card__desc">Fresh grains and bright greens with a quick lemon dressing.</p><span class="btn">MORE</span></article>
    <article class="card"><div class="thumb thumb--drink" role="img" aria-label="Photo of a green drink"></div><h3 class="card__title">Recipe title</h3><p class="card__meta">320 calories<br>25 min</p><p class="card__desc">Fresh grains and bright greens with a quick lemon dressing.</p><span class="btn">MORE</span></article>
  </div>
  <div class="grid" style="top:375px;left:46px;grid-template-columns:repeat(4,47px);column-gap:5.5px">
    <article class="card"><div class="thumb thumb--bowl" role="img" aria-label="Photo of a grain bowl"></div><h3 class="card__title">Recipe title</h3><p class="card__meta">320 calories<br>25 min</p><p class="card__desc">Fresh grains and bright greens with a quick lemon dressing.</p><span class="btn">MORE</span></article>
    <article class="card"><div class="thumb thumb--plate" role="img" aria-label="Photo of a plated main dish"></div><h3 class="card__title">Recipe title</h3><p class="card__meta">320 calories<br>25 min</p><p class="card__desc">Fresh grains and bright greens with a quick lemon dressing.</p><span class="btn">MORE</span></article>
    <article class="card"><div class="thumb thumb--crumble" role="img" aria-label="Photo of a baked dish on a spoon"></div><h3 class="card__title">Recipe title</h3><p class="card__meta">320 calories<br>25 min</p><p class="card__desc">Fresh grains and bright greens with a quick lemon dressing.</p><span class="btn">MORE</span></article>
    <article class="card"><div class="thumb thumb--drink" role="img" aria-label="Photo of a green drink"></div><h3 class="card__title">Recipe title</h3><p class="card__meta">320 calories<br>25 min</p><p class="card__desc">Fresh grains and bright greens with a quick lemon dressing.</p><span class="btn">MORE</span></article>
  </div>

  <nav class="pager"><span class="is-active">1</span><span>2</span><span>3</span><span>4</span><span>5</span><span>...</span><span>10</span><span>&gt;</span></nav>
</section>

<!-- RECIPE PAGE -->
<section class="page page--recipe">
  <div class="brand"><span class="brand__square"></span><span class="brand__name">PanFolio</span></div>
  <nav class="nav" style="top:74px"><span>MAIN</span><span class="sep">|</span><span>ABOUT</span><span class="sep">|</span><span>CONTACT</span></nav>

  <div class="abs category-tag" style="left:46px;top:98px">CATEGORY</div>
  <h1 class="abs recipe-title" style="left:46px;top:113px">RECIPE TITLE</h1>
  <div class="abs recipe-date" style="left:46px;top:126px">FEBRUARY 13 2012</div>
  <span class="btn btn--print">
    <svg width="5" height="4" viewBox="0 0 10 8" aria-hidden="true"><rect x="2" y="0" width="6" height="3" fill="#fff"/><rect x="0" y="3" width="10" height="3" fill="#fff"/><rect x="2" y="5" width="6" height="3" fill="#fff" stroke="#9c8f8a" stroke-width=".6"/></svg>
    PRINT
  </span>

  <div class="photo photo--detail-a" role="img" aria-label="Photo of baked granola on a wooden spoon"></div>
  <div class="photo photo--detail-b" role="img" aria-label="Photo of a bowl of granola with yogurt and berries"></div>

  <div class="facts">
    <h2>NUTRITIONAL FACTS</h2>
    <dl>
      <div><dt>Calories</dt><dd>875</dd></div>
      <div><dt>Fat</dt><dd>130g</dd></div>
      <div><dt>Carbohydrates</dt><dd>52g</dd></div>
      <div><dt>Protein</dt><dd>15g</dd></div>
      <div><dt>Cholesterol</dt><dd>0mg</dd></div>
      <div><dt>Vitamin A</dt><dd>1%</dd></div>
      <div><dt>Vitamin B</dt><dd>0%</dd></div>
      <div><dt>Vitamin C</dt><dd>0%</dd></div>
      <div><dt>Calcium</dt><dd>11%</dd></div>
      <div><dt>Iron</dt><dd>27%</dd></div>
      <div><dt>Sodium</dt><dd>20%</dd></div>
    </dl>
  </div>

  <h2 class="abs block-title" style="left:46px;top:313px">INGREDIENTS</h2>
  <p class="abs block-text" style="left:46px;top:330px;width:200px">The Morning Field Cereal<br>Grain Mix Base<br>1 cup quinoa<br>1 cup millet<br>4 ½ cups water<br>pinch of sea salt</p>

  <h2 class="abs block-title" style="left:46px;top:374px">DIRECTIONS</h2>
  <p class="abs block-text" style="left:46px;top:390px;width:206px">1. Rinse grains very well. Place in saucepan. Add water and salt.<br>2. Bring to a boil, reduce to simmer until water is absorbed, about 20 minutes.<br>3. Let cool slightly. Store in a container in the fridge tempora incidunt ut labore et dolore magnam aliquam quaerat voluptatem.</p>
</section>

</body>
</html>
```